Post Lockdown Ortho Special

We are running a special for (Ortho) Braces/Clear Aligner (Quorventa), till July 31st 2020. Up to $2,000 off with free Consultation and Xrays.

We need a ad to run in different formats.

Maybe something with: what better time to get braces when you have to wear a mask all the time.

Trying to rebuild our business and get people in for free consultations.

```html
<!DOCTYPE html>
<html lang="en">
<head>
<meta charset="utf-8">
<title>Pinecrest Family Dentistry – Ortho Special</title>
<link rel="stylesheet" href="https://fonts.googleapis.com/css2?family=Montserrat:wght@300;400;500;700;800;900&display=swap">
<style>
  :root {
    --paper: #f6f2fb;
    --purple: #6d4a9e;
    --purple-light: #8a6bbf;
    --ink: #3e3a44;
    --gold: #dbc30e;
    --white: #ffffff;
    --photo-a: #e9eef3;
    --photo-b: #c9ddeb;
    --photo-c: #d9c6e6;
  }
  html, body {
    margin: 0;
    padding: 0;
    overflow: hidden;
    background: var(--paper);
  }
  .ad {
    display: block;
    width: 1200px;
    height: 799px;
    font-family: "Montserrat", sans-serif;
  }
  .bg { fill: var(--paper); }
  .wave-light { fill: var(--purple-light); }
  .wave-dark { fill: var(--purple); }
  .brand-dot { fill: var(--purple); opacity: .18; }
  .brand-text { fill: var(--purple); font-weight: 500; }
  .brand-rule { stroke: var(--purple); stroke-width: 1; opacity: .6; }
  .offer-lead { fill: var(--purple); font-weight: 400; font-size: 31px; }
  .offer-amount { fill: var(--purple); font-weight: 800; }
  .badge-star { fill: var(--gold); stroke: var(--white); stroke-width: 12; stroke-linejoin: miter; }
  .badge-text { fill: var(--ink); }
  .badge-with { font-weight: 400; font-size: 27px; }
  .badge-free { font-weight: 900; font-size: 90px; }
  .badge-detail { font-weight: 800; font-size: 30px; }
  .photo-frame { stroke: var(--white); stroke-width: 7; }
  .deadline { fill: var(--white); font-weight: 400; font-size: 27px; }
  .phone-pill { fill: var(--white); }
  .phone-number { fill: var(--purple); font-weight: 800; font-size: 35px; }
</style>
</head>
<body>
<svg class="ad" viewBox="0 0 1200 799" xmlns="http://www.w3.org/2000/svg">
  <defs>
    <linearGradient id="photoTone" x1="0" y1="0" x2="1" y2="1">
      <stop offset="0" stop-color="var(--photo-a)"/>
      <stop offset=".6" stop-color="var(--photo-b)"/>
      <stop offset="1" stop-color="var(--photo-c)"/>
    </linearGradient>
  </defs>

  <rect class="bg" width="1200" height="799"/>

  <!-- bottom waves -->
  <path class="wave-light" d="M0,430 C60,560 140,625 230,624 C340,622 470,470 585,428 C640,418 680,450 705,490 L1200,490 L1200,799 L0,799 Z"/>
  <path class="wave-dark" d="M0,474 C70,545 130,562 200,562 C270,562 330,535 390,505 L700,505 C860,580 1080,470 1200,378 L1200,799 L0,799 Z"/>

  <!-- brand -->
  <g class="brand">
    <circle class="brand-dot" cx="170" cy="160" r="72"/>
    <text class="brand-text" x="272" y="158" font-size="50" textLength="294" lengthAdjust="spacingAndGlyphs">PINECREST</text>
    <text class="brand-text" x="272" y="181" font-size="16" textLength="294" lengthAdjust="spacing">FAMILY DENTISTRY</text>
    <line class="brand-rule" x1="272" y1="191" x2="566" y2="191"/>
    <text class="brand-text" x="300" y="212" font-size="15" textLength="235" lengthAdjust="spacing">DR HELENA MARSH</text>
  </g>

  <!-- offer -->
  <g class="offer">
    <text class="offer-lead" x="165" y="307">Up to</text>
    <text class="offer-amount" x="112" y="372" font-size="62">$</text>
    <text class="offer-amount" x="152" y="413" font-size="116" textLength="282" lengthAdjust="spacingAndGlyphs">2000</text>
    <text class="offer-amount" x="150" y="487" font-size="94" textLength="178" lengthAdjust="spacingAndGlyphs">OFF</text>
  </g>

  <!-- badge -->
  <g class="badge">
    <polygon class="badge-star" transform="translate(514 570) rotate(-8)"
      points="168,0 135.2,36.3 145.5,84 99,99 84,145.5 36.3,135.2 0,168 -36.3,135.2 -84,145.5 -99,99 -145.5,84 -135.2,36.3 -168,0 -135.2,-36.3 -145.5,-84 -99,-99 -84,-145.5 -36.3,-135.2 0,-168 36.3,-135.2 84,-145.5 99,-99 145.5,-84 135.2,-36.3"/>
    <text class="badge-text badge-with" x="482" y="491" textLength="66" lengthAdjust="spacingAndGlyphs">WITH</text>
    <text class="badge-text badge-free" x="417" y="566" textLength="200" lengthAdjust="spacingAndGlyphs">FREE</text>
    <text class="badge-text badge-detail" x="395" y="601" textLength="240" lengthAdjust="spacingAndGlyphs">CONSULTATION</text>
    <text class="badge-text badge-detail" x="427" y="627" textLength="177" lengthAdjust="spacingAndGlyphs">AND XRAYS</text>
  </g>

  <!-- photo area -->
  <path class="photo-frame" fill="url(#photoTone)" role="img"
    aria-label="Photo: dentist in blue scrubs and mask giving a patient a teeth whitening treatment in a dental chair"
    d="M700,205 C760,140 900,128 1010,140 C1125,153 1188,250 1186,360 C1184,470 1060,560 960,620 C880,667 790,668 745,603 C700,535 670,425 672,340 C673,280 680,235 700,205 Z"/>

  <!-- footer -->
  <text class="deadline" x="108" y="722" textLength="196" lengthAdjust="spacingAndGlyphs">Till July 31st 2020</text>
  <rect class="phone-pill" x="849" y="685" width="315" height="77" rx="38.5"/>
  <text class="phone-number" x="1006" y="736" text-anchor="middle" textLength="264" lengthAdjust="spacingAndGlyphs">(555) 310-4827</text>
</svg>
</body>
</html>
```